spoonful of caviar

I am looking to design a flyer/leaflet to distribute to houses or post on shop windows that invite people to buy caviar. The moto is: With our LOW prices you can now afford real CAVIAR by the SPOONFUL!
Customers will be offered three-four type of product or more on the website. There will be price advertised on the leaflet, brief description of the product and delivery terms: Free local delivery* (Wed & Fri, For more options: call 07831460925. The actual products are on the attached files and the theme ideas are there too.
Industry/Entity Type
Shop
Look and feel
Each slider illustrates characteristics of the customer's brand and the style your logo design should communicate.

```html
<!DOCTYPE html>
<html lang="en">
<head>
<meta charset="utf-8">
<title>Spoonful of Caviar – Leaflet</title>
<link href="https://fonts.googleapis.com/css2?family=Archivo+Black&family=Arimo:wght@400;700&display=swap" rel="stylesheet">
<style>
  :root{
    --stage:#6f6f6f;
    --orange:#f47a1f;
    --orange-deep:#e8600f;
    --orange-light:#fba63a;
    --roe:#f0561a;
    --red:#c8361b;
    --white:#ffffff;
    --photo-grey:#d2cfcb;
    --ink-red:#d8321c;
    --shade:rgba(110,35,0,.55);
  }
  *{margin:0;padding:0;box-sizing:border-box}
  html,body{width:1200px;height:1000px;overflow:hidden}
  body{background:var(--stage);font-family:"Arimo",Arial,sans-serif;position:relative}
  .page{position:absolute;overflow:hidden;box-shadow:5px 5px 6px rgba(0,0,0,.45)}
  .page--front{left:26px;top:33px;width:565px;height:730px;
    background:radial-gradient(circle at 30% 10%,var(--orange-light),var(--orange) 45%,var(--orange-deep))}
  .page--back{left:607px;top:224px;width:565px;height:730px;
    background:radial-gradient(circle at 60% 40%,var(--orange-light),var(--orange) 50%,var(--orange-deep))}
  .photo{position:absolute}
  .shapes{position:absolute;left:0;top:0}
  .txt{position:absolute;color:var(--white);font-weight:700;text-shadow:0 0 2px var(--shade)}

  .headline{left:0;width:565px;top:27px;text-align:center;font-family:"Archivo Black","Arimo",sans-serif;
    font-size:19.5px;line-height:25px;letter-spacing:.2px;font-weight:400;text-shadow:0 1px 2px rgba(120,40,0,.5)}
  .intro{left:0;width:565px;top:82px;text-align:center;font-size:12.5px;line-height:15px;font-weight:400}
  .gift-note{left:232px;top:310px;width:135px;font-size:13.5px;line-height:17px;font-weight:400}
  .section-title{left:42px;top:428px;font-family:"Archivo Black","Arimo",sans-serif;font-size:19px;font-weight:400;
    text-shadow:1px 1px 2px rgba(90,20,0,.6)}
  .body-copy{left:42px;top:461px;width:385px;font-size:10.4px;line-height:11.8px}
  .body-copy p+p{margin-top:12px}

  .back-h{font-size:14px;letter-spacing:.2px}
  .back-p{font-size:10px;line-height:11.9px}
  .pay-h{left:48px;top:40px}
  .pay-p{left:48px;top:70px;width:470px}
  .pay-p .lid-space{float:right;width:165px;height:128px;shape-outside:ellipse(100% 100% at 100% 0)}
  .ref-h{left:0;width:565px;top:266px;text-align:center}
  .ref-p{left:70px;top:295px;width:430px;text-align:center}
  .ship-h{left:48px;top:421px}
  .ship-p{left:48px;top:451px;width:470px}
  .ship-p .tart-space{float:left;width:240px;height:84px;shape-outside:polygon(0 0,30% 0,100% 100%,0 100%)}
  .ship-p .tail{display:block;text-align:right}
  .closing{left:278px;top:665px;width:237px;text-align:right;color:var(--ink-red);font-size:10.5px;line-height:12px;text-shadow:none}
</style>
</head>
<body>

<section class="page page--front">
  <svg class="shapes" width="565" height="730" viewBox="0 0 565 730" aria-hidden="true">
    <path d="M0 190 C160 150 340 130 565 132 L565 285 C380 280 170 295 0 330 Z" fill="var(--photo-grey)"/>
    <path d="M0 182 C160 142 340 122 565 126" stroke="var(--white)" stroke-width="12" fill="none"/>
    <path d="M0 330 C170 295 380 280 565 285" stroke="var(--red)" stroke-width="9" fill="none"/>
  </svg>
  <div class="photo" role="img" aria-label="Spoon heaped with orange salmon roe" style="left:150px;top:165px;width:320px;height:100px;border-radius:50%;background:radial-gradient(ellipse,var(--roe),rgba(240,86,26,0) 70%)"></div>
  <div class="photo" role="img" aria-label="Tin of keta caviar with roe at its base" style="left:44px;top:250px;width:180px;height:162px;border-radius:22px;background:linear-gradient(180deg,#f2f2f2 0%,#dcdcdc 55%,var(--roe) 80%,#c9421a 100%)"></div>
  <div class="photo" role="img" aria-label="Halved boiled eggs topped with red caviar and herbs on a white plate" style="left:345px;top:430px;width:220px;height:300px;background:radial-gradient(ellipse at 55% 55%,#f7f3ea 0%,#e8dccd 40%,rgba(240,86,26,.6) 75%,rgba(244,122,31,0) 100%)"></div>

  <h1 class="txt headline">WITH OUR LOW PRICES YOU CAN NOW<br>AFFORD REAL CAVIAR BY SPOON-FULL!!!</h1>
  <p class="txt intro">Please make sure you also view our &nbsp;other items and remember<br>to share positive feedback with us. &nbsp;We will do the same for you</p>
  <p class="txt gift-note">It would make a delicious addition to your party or an amazing and unique gift for any Occasion, too good to miss!!!</p>
  <h2 class="txt section-title">A Must Have for Russian Caviar Lovers!!!</h2>
  <div class="txt body-copy">
    <p>Look out for Keta Caviar! &nbsp;Of greatest value and quality,KetaCaviar has the riches taste and distinctly bigger, gorgeous, succulent roe grain. This delicacy is rich in Omega-3 polyunsaturated fats. Containing and combining all primary advantages of the caviar product, KetaCaviar is an undisputable supreme, world-renowned delicacy.</p>
    <p>Russian caviar has long been a delicacy for thousands of people. &nbsp;Our purchasing power allowed us to bring it to you at a price that would make you,your family and your friends enjoy it by spoon-full. &nbsp;To impress them even more, you can also buy the caviar pot souvenir from my other items and keep it as a reminder of delicious times!<br>Did I mention Omega-3 vitamin?!?!?!....<br>PLEAS NOTE: Actual Caviar colour and size might vary slightly from the photos provided as each harvest naturally differs.</p>
  </div>
</section>

<section class="page page--back">
  <svg class="shapes" width="565" height="730" viewBox="0 0 565 730" aria-hidden="true">
    <circle cx="455" cy="85" r="100" fill="rgba(255,220,170,.45)"/>
    <path d="M150 730 C250 650 420 620 565 600 L565 730 Z" fill="var(--white)"/>
    <path d="M200 640 C320 610 450 600 565 596" stroke="var(--red)" stroke-width="5" fill="none"/>
  </svg>
  <div class="photo" role="img" aria-label="Lid of a caviar tin seen from above" style="left:384px;top:12px;width:142px;height:142px;border-radius:50%;background:radial-gradient(circle,#2b2a4a 0%,#141426 60%,#b8913b 62%,#1c1c1c 70%)"></div>
  <div class="photo" role="img" aria-label="Pastry tartlets filled with cream and black and red caviar" style="left:0;top:570px;width:300px;height:160px;background:radial-gradient(ellipse at 40% 55%,#f6f1e8 0%,#d9a46b 45%,rgba(244,122,31,0) 80%)"></div>

  <h2 class="txt back-h pay-h">PAYMENTS, HANDLING &amp; SHIPPING</h2>
  <p class="txt back-p pay-p"><span class="lid-space"></span>If you pay by PayNest we will do our best to send your goods the next day, or if it is the weekend - on Monday. &nbsp;All items shipped chilled from England UK and are traceable and/or insured. To all International buyers: Please don't be put off by the fact that items are shipped from England. Your order will be traceable and I always use optimal shipping means e.g. Crown Post, ParcelWay, SwiftFreight, TransNet, Herald Parcels.<br>Reduced shipping cost on multiple items posted together. Please, wait for total from us as overpayment for the postage cannot be refunded. We also accept other means of payments like bank transfers and international IBAN payments. &nbsp;Contact us prior to purchasing for advice on best payment options. In the unlikely event that your order is damaged in transit, please send us the pictures of the damage to allow us to claim compensation from shipping company. &nbsp;We will gladly replace the item at no additional charge.</p>

  <h2 class="txt back-h ref-h">REFUNDS &amp; WARRANTEES</h2>
  <p class="txt back-p ref-p">Refund policy: regretfully, we are unable to offer a refund once the order is opened. Products are storable for 6 months and must be consumed within 2 weeks of opening. You will be so pleased with the taste that you would never want to return it. &nbsp;We take feedback very seriously, please remember if you are not happy with our service, then please contact us.<br>Please check out my other items and see more unique and interesting things for you. Please leave feedback once you have received the item so that I know it has arrived safely. I will leave feedback in return.</p>

  <h2 class="txt back-h ship-h">SHIPPING AND PACKAGING INFORMATION:</h2>
  <div class="txt back-p ship-p">We ship in the UK and Worldwide and always use traceable quality services (TransNet, DeltaHaul, ParcelWay, Crown Post and Herald Parcels) for items with the value exceeding 10 GBP. &nbsp;International shipping will be charged accordingly. &nbsp;Collections in person and cash payments are welcome. Please contact me prior to purchasing should you have other shipping preferences.<br>In the unlikely event that your order is delivered damaged, kindly take pictures of damaged packaging and/or product and forward them to us to allow us to claim compensation from the courier. &nbsp;We will happily replace damaged item once it is returned to us at no extra
    <span class="tart-space"></span><span class="tail">charge. &nbsp;In most cases we will compensate your return shipping cost up to 5.00 GBP. &nbsp;Never hesitate to contact us should any questions arise. Always contact us via email should any questions, queries, suggestions or complaints arise. &nbsp;We aim to please our customers and will endeavour to resolve any reasonable issues according to specified terms and conditions.</span></div>

  <p class="txt closing">Please make sure you view our &nbsp;other items and remember to share positive feedback with us. &nbsp;We will do the same for you</p>
</section>

</body>
</html>
```